Tolvern Business Cards

Business card design. dont mind if new logo is suggested.
it would be for a security company.
our clients would be bigger security companies around Australia.
have a logo done but can be replaced. see attaached. like the colors.
Need company name, person name, designation, phone and email on front.
At back company logo and name. website saddress and 2 x license numbers
would like to have 2 different background color for both sidde

Industry/Entity Type

Security

Contact Information for Business Card

round corners, front should be light in color. need logo at back with webaddress and 2 x license numners

Font styles to use
Sans Serif

Colors
f37122
faa54b
f8ba93
0255a3
0592cd
85cae6
b3d448
9bcb3c
ffffff

Requirements
Must have
• see description
Nice to have
• see description
Should not have
• should not be difficult to read or hardd to find information on card.. lets say easy on eyes yet catchy

```html
<!DOCTYPE html>
<html lang="en">
<head>
<meta charset="UTF-8">
<title>Tolvern Security Group – Business Cards</title>
<link href="https://fonts.googleapis.com/css2?family=Roboto:wght@400;700&family=Noto+Serif:wght@400&display=swap" rel="stylesheet">
<style>
  :root {
    --bg: #5b6166;
    --bg-light: #80868b;
    --card-blue: #06a5cc;
    --navy: #1d2d6b;
    --white: #ffffff;
    --ink: #1b1f24;
    --card-w: 640px;
    --card-h: 366px;
    --radius: 22px;
  }
  * { box-sizing: border-box; margin: 0; padding: 0; }
  html, body { width: 1200px; height: 900px; overflow: hidden; }
  body {
    background: radial-gradient(ellipse at 45% 40%, var(--bg-light), var(--bg) 75%);
    font-family: "Roboto", Arial, sans-serif;
    position: relative;
  }
  .card {
    position: absolute;
    left: 280px;
    width: var(--card-w);
    height: var(--card-h);
    border-radius: var(--radius);
    overflow: hidden;
    box-shadow: 0 10px 24px rgba(0,0,0,.35);
  }
  .card--front { top: 54px; background: var(--card-blue); }
  .card--back  { top: 480px; background: var(--card-blue); }

  .front-shape { position: absolute; inset: 0; }

  .contact {
    position: absolute;
    left: 40px;
    top: 42px;
    color: var(--white);
  }
  .contact__name { font-size: 27px; font-weight: 700; letter-spacing: .2px; }
  .contact__role { font-size: 14px; margin-top: 2px; opacity: .95; }
  .contact__list { list-style: none; margin-top: 26px; font-size: 15px; line-height: 1.55; }
  .contact__list li { display: flex; align-items: flex-start; gap: 10px; }
  .contact__list svg { width: 14px; height: 14px; margin-top: 4px; flex: none; fill: var(--white); }

  .brand {
    position: absolute;
    display: flex;
    align-items: center;
    font-family: "Noto Serif", Georgia, serif;
    font-weight: 400;
    letter-spacing: 1px;
    white-space: nowrap;
  }
  .brand__dot { border-radius: 50%; flex: none; }
  .brand--front {
    left: 362px; right: 22px; top: 112px;
    flex-direction: column; justify-content: center; gap: 16px;
    color: var(--navy); font-size: 18px;
  }
  .brand--front .brand__dot { width: 62px; height: 62px; background: var(--card-blue); }
  .brand--back {
    left: 50%; top: 50%; transform: translate(-50%, -60%);
    flex-direction: column; gap: 18px; color: var(--white); font-size: 34px;
  }
  .brand--back .brand__dot { width: 70px; height: 70px; background: var(--white); }

  .back-web {
    position: absolute; left: 34px; bottom: 30px;
    color: var(--ink); font-size: 15px;
  }
  .back-licenses {
    position: absolute; right: 34px; bottom: 26px;
    color: var(--ink); font-size: 18px; line-height: 1.2; text-align: right;
  }
</style>
</head>
<body>

<section class="card card--front" aria-label="Card front">
  <svg class="front-shape" viewBox="0 0 640 366" preserveAspectRatio="none">
    <path d="M448 0 Q318 110 340 366 L640 366 L640 0 Z" fill="var(--white)"/>
    <path d="M432 0 Q300 110 322 366" fill="none" stroke="var(--navy)" stroke-width="7"/>
  </svg>

  <div class="contact">
    <h1 class="contact__name">Darian Kellow</h1>
    <p class="contact__role">Owner</p>
    <ul class="contact__list">
      <li><svg viewBox="0 0 24 24"><path d="M6.6 10.8a15 15 0 0 0 6.6 6.6l2.2-2.2c.3-.3.7-.4 1-.2 1.1.4 2.3.6 3.6.6.6 0 1 .4 1 1V20c0 .6-.4 1-1 1A17 17 0 0 1 3 4c0-.6.4-1 1-1h3.5c.6 0 1 .4 1 1 0 1.3.2 2.5.6 3.6.1.3 0 .7-.2 1z"/></svg>555-201-7788</li>
      <li><svg viewBox="0 0 24 24"><path d="M7 1h10a2 2 0 0 1 2 2v18a2 2 0 0 1-2 2H7a2 2 0 0 1-2-2V3a2 2 0 0 1 2-2zm0 3v15h10V4z"/></svg>555-201-7790</li>
      <li><svg viewBox="0 0 24 24"><path d="M2 5h20v14H2zm2 2v.4l8 5 8-5V7zm0 2.8V17h16V9.8l-8 5z"/></svg>darian@tolvernsg.com</li>
      <li><svg viewBox="0 0 24 24"><path d="M12 2a10 10 0 1 0 0 20 10 10 0 0 0 0-20zm0 2a8 8 0 0 1 7.4 5H15a13 13 0 0 0-1.5-4.9A8 8 0 0 1 12 4zm-3 13H4.6A8 8 0 0 1 4 12h5a20 20 0 0 0 0 5zm2 0a18 18 0 0 1 0-5h2a18 18 0 0 1 0 5z"/></svg>www.tolvernsg.com</li>
      <li><svg viewBox="0 0 24 24"><path d="M12 2a7 7 0 0 0-7 7c0 5 7 13 7 13s7-8 7-13a7 7 0 0 0-7-7zm0 9.5A2.5 2.5 0 1 1 12 6a2.5 2.5 0 0 1 0 5.5z"/></svg><span>48 Harbour Row<br>Geelong VIC 3220</span></li>
    </ul>
  </div>

  <div class="brand brand--front">
    <span class="brand__dot"></span>
    <span class="brand__name">TOLVERN SECURITY GROUP</span>
  </div>
</section>

<section class="card card--back" aria-label="Card back">
  <div class="brand brand--back">
    <span class="brand__dot"></span>
    <span class="brand__name">TOLVERN SECURITY GROUP</span>
  </div>
  <p class="back-web">www.tolvernsg.com</p>
  <p class="back-licenses">License #1<br>License #2</p>
</section>

</body>
</html>
```